Plakat für Schaufenster
Zielgruppe
Moin Moin,
ich habe einen kleinen Fahrradladen in einem historischen Gebäude. Wir führen ein sehr hochwertiges und ausgesuchtes Programm diverser Hersteller und bieten eine umfassende individuelle Beratung
Aufgabenstellung
Ein Fahrradladen ist einerseits ein Handwerksbetrieb anderseits auch ein Handelsbetrieb. Da ich als Einzelkämpfer in meinem Laden arbeite, habe ich diese beiden Betriebe zeitlich voneinander getrennt. Ich arbeite Vormittags in der Werkstatt und Nachmitttags ist mein Laden für Service und Beratung geöffnet, d.h. meine Laden ist nur Nachmittags von 14-18 und Samstag von 10-13 Uhr geöffnet. Durch diese Regelung kann ich kurze Reparaturzeiten und gute Beratung bieten.
Leider denken nun viele Menschen wenn Sie Vormittags vor verschlossener Tür stehen: "der hat es nicht nötig und arbeitet nur noch halbe Tage!".
Nun möchte ich mit einem Plakat im Fenster meinen "geteilten" Betrieb bzw. meine Arbeitsteilung erklären.
Vielleicht in Form einer analogen Uhr mit entsprechender Teilung !?! Aber auch andere Ideen sind herzlich Willkommen !!

```html
<!DOCTYPE html>
<html lang="de">
<head>
<meta charset="utf-8">
<title>Werkstattzeiten &amp; Öffnungszeiten</title>
<link href="https://fonts.googleapis.com/css2?family=Big+Shoulders+Display:wght@500;600&display=swap" rel="stylesheet">
<style>
  :root {
    --paper: #e7d7c5;
    --green-dark: #0f5a2f;
    --green-light: #1f8e4b;
    --frame-green: #1b7a3f;
    --taupe: #a68f80;
    --ink: #3b3734;
  }
  html, body {
    margin: 0;
    padding: 0;
    width: 872px;
    height: 1200px;
    overflow: hidden;
    background: var(--paper);
  }
  .poster {
    display: block;
    width: 872px;
    height: 1200px;
  }
  .headline {
    font-family: "Big Shoulders Display", "Oswald", sans-serif;
    font-weight: 600;
    text-transform: uppercase;
  }
  .headline--workshop { fill: var(--green-dark); }
  .headline--opening { fill: var(--green-light); }
  .hours {
    font-family: "Big Shoulders Display", "Oswald", sans-serif;
    font-weight: 500;
    fill: var(--ink);
    text-transform: uppercase;
  }
  .services {
    font-family: "Big Shoulders Display", "Oswald", sans-serif;
    font-weight: 500;
    fill: var(--taupe);
    text-transform: uppercase;
  }
  .info-box {
    fill: none;
    stroke: var(--frame-green);
    stroke-width: 2.5;
  }
</style>
</head>
<body>
<svg class="poster" viewBox="0 0 872 1200" xmlns="http://www.w3.org/2000/svg">
  <defs>
    <radialGradient id="illustration-tone" cx="579" cy="564" r="420" gradientUnits="userSpaceOnUse">
      <stop offset="0" stop-color="#a68f80"/>
      <stop offset="0.28" stop-color="#3f7a52"/>
      <stop offset="0.55" stop-color="#c9b9a8"/>
      <stop offset="1" stop-color="#e7d7c5"/>
    </radialGradient>
  </defs>

  <rect class="paper" width="872" height="1200" fill="var(--paper)"/>

  <!-- illustration area -->
  <rect class="clock-bicycle-illustration" role="img"
        aria-label="Illustration: vintage bicycle behind an alarm clock whose dial is split into workshop and opening hours, with a gear and crank at its centre"
        x="0" y="300" width="780" height="500" fill="url(#illustration-tone)"/>

  <!-- workshop hours box -->
  <g class="workshop-hours">
    <rect class="info-box" x="58" y="34" width="534" height="295" fill="var(--paper)"/>
    <line class="info-box" x1="58" y1="199" x2="592" y2="199"/>
    <line class="info-box" x1="592" y1="329" x2="592" y2="362"/>
    <text class="headline headline--workshop" x="96" y="165" font-size="122" textLength="466" lengthAdjust="spacingAndGlyphs">Werkstattzeiten</text>
    <text class="hours" x="96" y="293" font-size="68" textLength="328" lengthAdjust="spacingAndGlyphs">Di - Fr // Vormittag</text>
  </g>

  <!-- connector to opening hours -->
  <line class="info-box" x1="579" y1="767" x2="579" y2="795"/>

  <!-- opening hours box -->
  <g class="opening-hours">
    <rect class="info-box" x="334" y="795" width="480" height="368"/>
    <line class="info-box" x1="334" y1="959" x2="814" y2="959"/>
    <text class="headline headline--opening" x="374" y="925" font-size="122" textLength="408" lengthAdjust="spacingAndGlyphs">Öffnungszeiten</text>
    <text class="hours" x="782" y="1056" font-size="70" text-anchor="end" textLength="312" lengthAdjust="spacingAndGlyphs">Di - Fr // 14 - 18 Uhr</text>
    <text class="hours" x="782" y="1132" font-size="70" text-anchor="end" textLength="254" lengthAdjust="spacingAndGlyphs">Sa // 10 - 13 Uhr</text>
  </g>

  <!-- services list -->
  <g class="services-list">
    <text class="services" x="307" y="1006" font-size="80" text-anchor="end" textLength="189" lengthAdjust="spacingAndGlyphs">Fahrräder</text>
    <text class="services" x="307" y="1084" font-size="80" text-anchor="end" textLength="142" lengthAdjust="spacingAndGlyphs">Service</text>
    <text class="services" x="307" y="1161" font-size="80" text-anchor="end" textLength="134" lengthAdjust="spacingAndGlyphs">Verleih</text>
  </g>
</svg>
</body>
</html>
```